OKRUVI card Technical Architecture

Hello everyone OKRUVI: It is a consulting firm in Architecture and Construction. I require a card duplexing, sober, elegant, classic but not boring. Update 1: Use the following data for the card. Name: Rodrigo Salcedo Mauricio Quintana Position: COO Twitter: @okruviTB Homepage: okruvi.net home address not include the participation of all thank you.

Target Market(s)

Construction companies, Architects and Consulting Engineers

Industry/Entity Type

Consulting

Contact Information for Business Card

Los campos que debe tener:
Nombre, Cargo, email, homepage y twitter

Font styles to use
Serif
Sans Serif
Other font styles liked:
• Me gustan playfair display, open sans y roboto, pero estoy sujeto a sus propuestas

Requirements
Must have
• Colors: Present combined proposals in white, red, gray and black Update 1: The two names must be clearly differentiated from the two surnames
Nice to have
• They are free to present their best proposals. I will bring them immediate feedback to the extent you can go see their designs. Complete data for card and logo files will give the winner the

```html
<!DOCTYPE html>
<html lang="es">
<head>
<meta charset="utf-8">
<title>OKRUVI — Tarjeta de presentación</title>
<link rel="stylesheet" href="https://fonts.googleapis.com/css2?family=Montserrat:wght@400&family=Open+Sans:wght@400&family=Playfair+Display:wght@500&display=swap">
<style>
  :root {
    --backdrop: #3a332f;
    --card: #141414;
    --card-edge: #1e1e1e;
    --red: #b3141c;
    --red-soft: #8e1118;
    --white: #f4f4f4;
    --gray: #9a9a9a;
  }
  * { box-sizing: border-box; margin: 0; padding: 0; }
  html, body { width: 1200px; height: 780px; overflow: hidden; }
  body { background: var(--backdrop); position: relative; font-family: "Open Sans", sans-serif; }

  .card {
    position: absolute;
    width: 540px;
    height: 310px;
    background: var(--card);
    border: 1px solid var(--card-edge);
    border-radius: 4px;
    box-shadow: 0 18px 40px rgba(0,0,0,.45);
  }
  .card--front { left: 50px; top: 90px; }
  .card--back { left: 610px; top: 380px; }

  .brand { position: absolute; }
  .card--front .brand { left: 90px; top: 100px; }
  .card--back .brand { left: 34px; top: 110px; }

  .brand__name {
    display: flex;
    align-items: center;
    gap: 14px;
    font-family: "Montserrat", sans-serif;
    font-weight: 400;
    color: var(--white);
    letter-spacing: 0.42em;
    line-height: 1;
  }
  .card--front .brand__name { font-size: 44px; }
  .card--back .brand__name { font-size: 30px; gap: 10px; }
  .brand__mark { background: var(--red); flex: none; }
  .card--front .brand__mark { width: 14px; height: 14px; }
  .card--back .brand__mark { width: 10px; height: 10px; }

  .brand__rule { height: 1px; background: var(--red-soft); margin-top: 10px; }
  .brand__tagline {
    font-family: "Montserrat", sans-serif;
    color: var(--red);
    text-transform: uppercase;
    letter-spacing: 0.3em;
    margin-top: 6px;
  }
  .card--front .brand__tagline { font-size: 13px; }
  .card--back .brand__tagline { font-size: 9px; }

  .divider {
    position: absolute;
    left: 272px; top: 60px;
    width: 1.5px; height: 190px;
    background: var(--red-soft);
  }
  .person { position: absolute; left: 292px; top: 70px; }
  .person__name {
    font-family: "Playfair Display", serif;
    font-weight: 500;
    color: var(--red);
    font-size: 19px;
    line-height: 1.05;
  }
  .person__role { font-size: 12px; color: var(--red); margin-top: 3px; }

  .contact { position: absolute; left: 292px; top: 170px; list-style: none; }
  .contact__item {
    display: flex; align-items: center; gap: 10px;
    color: var(--white); font-size: 15px; line-height: 22px;
  }
  .contact__icon { width: 11px; height: 11px; flex: none; }
</style>
</head>
<body>

<section class="card card--front">
  <div class="brand">
    <div class="brand__name"><span>OKRUVI</span><span class="brand__mark"></span></div>
    <div class="brand__rule"></div>
    <div class="brand__tagline">Arquitectura Técnica</div>
  </div>
</section>

<section class="card card--back">
  <div class="brand">
    <div class="brand__name"><span>OKRUVI</span><span class="brand__mark"></span></div>
    <div class="brand__rule"></div>
    <div class="brand__tagline">Arquitectura Técnica</div>
  </div>

  <div class="divider"></div>

  <div class="person">
    <p class="person__name">Mauricio Rodrigo<br>Salcedo Quintana</p>
    <p class="person__role">Director de Operaciones</p>
  </div>

  <ul class="contact">
    <li class="contact__item">
      <svg class="contact__icon" viewBox="0 0 12 12" aria-hidden="true">
        <rect width="12" height="12" rx="2" fill="#b3141c"/>
        <path d="M3.6 2.6l1.2 1.6-.7.9c.5 1 1.2 1.7 2.2 2.2l.9-.7 1.6 1.2-.6 1.4C5.7 9 3 6.3 2.2 3.2z" fill="#141414"/>
      </svg>
      (+572) 555 010 2030
    </li>
    <li class="contact__item">
      <svg class="contact__icon" viewBox="0 0 12 12" aria-hidden="true">
        <rect width="12" height="12" rx="2" fill="#b3141c"/>
        <circle cx="6" cy="6" r="3.4" fill="none" stroke="#141414" stroke-width="1"/>
        <path d="M2.6 6h6.8M6 2.6c-1.6 2-1.6 4.8 0 6.8M6 2.6c1.6 2 1.6 4.8 0 6.8" fill="none" stroke="#141414" stroke-width=".8"/>
      </svg>
      okruvi.net
    </li>
    <li class="contact__item">
      <svg class="contact__icon" viewBox="0 0 12 12" aria-hidden="true">
        <rect width="12" height="12" rx="2" fill="#b3141c"/>
        <circle cx="6" cy="6" r="2.6" fill="#141414"/>
      </svg>
      @okruviTB
    </li>
  </ul>
</section>

</body>
</html>
```